Business Card Design for Orthopaedic Surgeon

This is a double-sided glossy business card. I prefer baby blue, teal, and green as color schemes. I have my logo already (many colors that you can choose from). I have photos and examples of my old card (very bland but has the information in it). I also have one that my assistant tried to design, but the writing is too small and I don't love the formatting. But it is close!
I would like my logo to be on the business card but I'm uploading my logo in many different colors so you can choose which one looks best based on the color scheme. I also uploaded many sized headshots so you can choose the best resolution one.

Additional information:
Correct business address:
4382 NW 58th Lane, Suite 305
Tamarac, FL 33417

Everything else on both business cards are accurate.

I actually need 2 different business cards generated. One that includes my cell phone number-- Personal cell: 585-314-9062 in addition to Office phone: (954) 316-4870 and Office Fax: 954-316-4881. Again, one card would have my personal cell and one wouldn't

Overall I just think the baby blue card (uploaded) is missing something on the front--of course it is also missing my office phone/fax/personal cell. I do want my website on the front too. Email: info@wellsorthocare.example

You can use your discretion about what goes on the front vs. what goes on the back to eliminated clutter.

Oh and on the back, I would like to list "Conditions Treated" (not specialties include). The list is:
Carpal Tunnel
Trigger Finger
Ganglion Cysts
Hand Tumors
Han & Wrist Arthritis
Hand, Wrist & Elbow Tendonitis
Fractures of the Hand, Wrist, Elbow and Humerus
Nerve Injuries of the Hand, Wrist & Elbow
Microsurgery
Wrist Arthroscopy
Endoscopic Surgery

Target Market(s)

Primary care doctors, Lawyers, patients

Industry/Entity Type

Medical

Contact Information for Business Card

Please see above in project description

Colors

Designer to choose colors to be used in the design.

Requirements
Must have
• -Correct office info, Board Certified Orthopaedic Hand & Upper Extremity Surgeon
Nice to have
• Something that is classy and wow!

```html
<!DOCTYPE html>
<html lang="en">
<head>
<meta charset="utf-8">
<title>Dana Wells, MD – Business Card</title>
<link href="https://fonts.googleapis.com/css2?family=Montserrat:wght@400;500;600&family=Oswald:wght@500&display=swap" rel="stylesheet">
<style>
  :root {
    --navy: #141f4f;
    --sky: #27a6df;
    --ink: #1b1f2e;
    --rule: #8a90ad;
    --paper: #ffffff;
    --stage: #3a3a3c;
  }
  * { box-sizing: border-box; margin: 0; padding: 0; }
  html, body { width: 1200px; height: 1200px; overflow: hidden; }
  body {
    background: var(--stage);
    font-family: "Montserrat", sans-serif;
    display: flex; flex-direction: column; align-items: center; justify-content: center; gap: 56px;
  }
  .card {
    position: relative; width: 900px; height: 514px; border-radius: 34px; overflow: hidden;
  }
  /* Front */
  .card-front { background: var(--paper); color: var(--ink); }
  .card-front .wave { position: absolute; inset: 0; }
  .identity { position: absolute; left: 64px; top: 112px; }
  .name { color: var(--sky); font-size: 40px; font-weight: 500; letter-spacing: .5px; line-height: 1; }
  .title { font-size: 15px; font-weight: 500; text-transform: uppercase; line-height: 1.15; margin-top: 8px; letter-spacing: .3px; }
  .contacts { position: absolute; left: 64px; top: 214px; list-style: none; font-size: 19px; }
  .contacts li { display: flex; align-items: flex-start; gap: 14px; line-height: 1.2; margin-bottom: 7px; }
  .contacts svg { width: 22px; height: 22px; flex: none; margin-top: 1px; fill: var(--sky); }
  .contacts .label { color: var(--sky); font-size: 14px; }
  .contacts .sep { color: var(--rule); margin: 0 6px; }
  .divider { position: absolute; left: 520px; top: 70px; width: 1px; height: 230px; background: #b9bccb; transform: rotate(-14deg); }
  .portrait {
    position: absolute; left: 560px; top: 40px; width: 250px; height: 250px; border-radius: 50%;
    border: 4px solid var(--sky); padding: 8px;
  }
  .portrait span { display: block; width: 100%; height: 100%; border-radius: 50%; background: radial-gradient(circle at 50% 40%, #8a6a58, #1e1a1c 75%); }
  .website { position: absolute; left: 300px; bottom: 30px; color: var(--paper); font-size: 22px; letter-spacing: .5px; }
  .website b { color: var(--sky); font-weight: 400; }
  /* Back */
  .card-back { background: linear-gradient(135deg, #121c4a, #1a2a63 55%, #131d4b); color: var(--paper); }
  .brand { position: absolute; left: 50%; top: 46px; transform: translateX(-50%); display: flex; align-items: center; gap: 16px; }
  .brand-circle { width: 150px; height: 150px; border-radius: 50%; border: 6px solid var(--sky); }
  .brand-name { color: var(--sky); font-size: 34px; font-weight: 600; letter-spacing: 4px; }
  .conditions-head { position: absolute; left: 0; right: 0; top: 248px; display: flex; align-items: center; gap: 20px; padding: 0 60px; }
  .conditions-head hr { flex: 1; border: 0; border-top: 1.5px solid var(--rule); }
  .conditions-head h2 { font-size: 26px; font-weight: 500; letter-spacing: 1px; }
  .lists { position: absolute; left: 60px; right: 40px; top: 310px; display: grid; grid-template-columns: 200px 290px 1fr; gap: 24px; }
  .lists ul { list-style: none; font-family: "Oswald", sans-serif; font-weight: 500; font-size: 19px; line-height: 1.2; text-transform: uppercase; letter-spacing: -.2px; }
  .lists li { position: relative; padding-left: 16px; }
  .lists li::before { content: ""; position: absolute; left: 0; top: 9px; width: 7px; height: 7px; border-radius: 50%; background: var(--sky); }
</style>
</head>
<body>
  <section class="card card-front">
    <svg class="wave" viewBox="0 0 900 514" aria-hidden="true">
      <path d="M540 432 C 720 405, 840 330, 900 175 L 900 222 C 830 340, 720 410, 540 432 Z" fill="var(--sky)"/>
      <path d="M180 514 C 280 420, 470 440, 640 400 C 780 368, 870 300, 900 238 L 900 514 Z" fill="var(--navy)"/>
    </svg>
    <div class="identity">
      <h1 class="name">DANA WELLS, MD</h1>
      <p class="title">Board Certified Orthopaedic<br>Hand &amp; Upper Extremity Surgeon</p>
    </div>
    <ul class="contacts">
      <li><svg viewBox="0 0 24 24"><path d="M7 1h10a2 2 0 0 1 2 2v18a2 2 0 0 1-2 2H7a2 2 0 0 1-2-2V3a2 2 0 0 1 2-2zm0 3v14h10V4zm5 15.5a1 1 0 1 0 0 2 1 1 0 0 0 0-2z"/></svg><span>585-314-9062</span></li>
      <li><svg viewBox="0 0 24 24"><path d="M6.6 10.8a15 15 0 0 0 6.6 6.6l2.2-2.2a1 1 0 0 1 1-.25 11.4 11.4 0 0 0 3.6.57 1 1 0 0 1 1 1V20a1 1 0 0 1-1 1A17 17 0 0 1 3 4a1 1 0 0 1 1-1h3.5a1 1 0 0 1 1 1c0 1.25.2 2.45.57 3.6a1 1 0 0 1-.25 1z"/></svg><span>(954) 316-4870<span class="sep">|</span><span class="label">Fax: </span>(954) 316-4881</span></li>
      <li><svg viewBox="0 0 24 24"><path d="M2 5h20v14H2zm2 2v.4l8 5 8-5V7zm0 2.8V17h16V9.8l-8 5z"/></svg><span>info@wellsorthocare.example</span></li>
      <li><svg viewBox="0 0 24 24"><path d="M12 1a8 8 0 0 0-8 8c0 6 8 14 8 14s8-8 8-14a8 8 0 0 0-8-8zm0 11a3 3 0 1 1 0-6 3 3 0 0 1 0 6z"/></svg><span>4382 NW 58th Lane, Suite 305<br>Tamarac, FL 33417</span></li>
    </ul>
    <div class="divider"></div>
    <div class="portrait"><span role="img" aria-label="Headshot of Dr. Dana Wells"></span></div>
    <p class="website">WWW.<b>WELLSORTHOCARE</b>.EXAMPLE</p>
  </section>

  <section class="card card-back">
    <div class="brand">
      <span class="brand-circle"></span>
      <span class="brand-name">WELLS HAND</span>
    </div>
    <div class="conditions-head"><hr><h2>CONDITIONS TREATED</h2><hr></div>
    <div class="lists">
      <ul>
        <li>Carpal Tunnel</li>
        <li>Trigger Finger</li>
        <li>Ganglion Cysts</li>
        <li>Hand Tumors</li>
      </ul>
      <ul>
        <li>Han &amp; Wrist Arthritis</li>
        <li>Hand, Wrist &amp; Elbow Tendonitis</li>
        <li>Fractures of the Hand, Wrist, Elbow and Humerus</li>
      </ul>
      <ul>
        <li>Nerve Injuries of the Hand, Wrist &amp; Elbow</li>
        <li>Microsurgery</li>
        <li>Wrist Arthroscopy</li>
        <li>Endoscopic Surgery</li>
      </ul>
    </div>
  </section>
</body>
</html>
```